Business card design needed

www.corvanfab.com.au
Our primary services:
On-site welding.
On-site industrial maintenance.
On-site repairs and capital works projects specialising in pipe fabrication.
Our ability to work on-site with our dedicated mobile equipment is essential to our capability to provide a quality maintenance service to our customers. We are capable of providing a full team of qualified boilermakers that can work either to your plan or project manage if a plan has not been developed.
Industry/Entity Type
Industrial
Contact Information for Business Card
company name- CORVAN FAB PTY LTD
story - industrial steel fabrication, constructions and pipelines
Director - Greg Halvey
workshop address - shed 7, 3820 mirren rd Tully
postal address - P.O BOX 268 WARRINBAH Q 4861
mobile - 0438596204
w/shop phone - 0740593827
fax - 0740593828
email - admin@corvanfab.com.au
web - www.corvanfab.com.au
Logo Text
CORVAN FAB pty ltd

```html
<!DOCTYPE html>
<html lang="en">
<head>
<meta charset="utf-8">
<title>Corvan Fab Business Card</title>
<link rel="stylesheet" href="https://fonts.googleapis.com/css2?family=Arimo:ital,wght@0,400;0,700;1,400&display=swap">
<style>
  :root {
    --brand-blue: #243f92;
    --ink: #1a1a1a;
    --steel-light: #e8e9ec;
    --steel-mid: #cfd1d6;
    --steel-dark: #8a8e97;
    --page: #ffffff;
    --card-edge: #2b2b2b;
  }
  html, body {
    margin: 0; padding: 0;
    width: 1200px; height: 1200px;
    overflow: hidden;
    background: var(--page);
    font-family: "Arimo", Arial, sans-serif;
  }
  .card {
    position: absolute;
    left: 58px; top: 330px;
    width: 1064px; height: 614px;
    box-sizing: border-box;
    border: 1px solid var(--card-edge);
    background: var(--page);
    box-shadow: 6px 8px 14px rgba(0,0,0,0.12);
    overflow: hidden;
  }
  .card-art { position: absolute; inset: 0; width: 100%; height: 100%; }
  .brand-name {
    position: absolute;
    left: 90px; top: 236px;
    width: 320px;
    margin: 0;
    font-size: 52px;
    font-weight: 400;
    line-height: 1;
    letter-spacing: -1px;
    color: var(--brand-blue);
    text-align: center;
    white-space: nowrap;
  }
  .tagline {
    position: absolute;
    left: 90px; top: 354px;
    margin: 0;
    font-size: 25px;
    font-style: italic;
    line-height: 30px;
    color: var(--brand-blue);
    white-space: nowrap;
  }
  .contact {
    position: absolute;
    right: 45px;
    color: var(--ink);
    font-size: 28px;
    line-height: 35px;
    text-align: right;
  }
  .person { top: 104px; }
  .person-name {
    margin: 0;
    font-size: 32px;
    font-weight: 700;
    line-height: 36px;
    color: var(--brand-blue);
  }
  .person-role { margin: 0; font-size: 28px; line-height: 34px; }
  .address { top: 250px; font-style: normal; }
  .lines { top: 400px; margin: 0; padding: 0; list-style: none; }
  .line { display: flex; justify-content: space-between; }
  .line-phone { width: 236px; margin-left: auto; }
  .line-web { width: 386px; }
  .label { font-weight: 700; color: var(--brand-blue); }
</style>
</head>
<body>
  <div class="card">
    <svg class="card-art" viewBox="0 0 1064 614">
      <defs>
        <linearGradient id="steel" x1="0" y1="1" x2="0.9" y2="0">
          <stop offset="0" stop-color="var(--steel-mid)"/>
          <stop offset="0.5" stop-color="var(--steel-light)"/>
          <stop offset="0.8" stop-color="var(--steel-mid)"/>
          <stop offset="1" stop-color="var(--steel-dark)"/>
        </linearGradient>
      </defs>
      <polygon role="img" aria-label="Brushed stainless steel texture" points="0,0 578,0 397,614 0,614" fill="url(#steel)"/>
      <polygon class="accent-band" points="578,0 611,0 432,614 397,614" fill="var(--brand-blue)"/>
    </svg>

    <p class="brand-name">CORVAN FAB</p>
    <p class="tagline">Industrial steel fabrication,<br>constructions and pipelines</p>

    <div class="contact person">
      <p class="person-name">Greg Halvey</p>
      <p class="person-role">DIRECTOR</p>
    </div>

    <address class="contact address">
      Shed 7, 3820 Mirren Rd<br>
      (PO BOX 268)<br>
      WARRINBAH NQ 4861
    </address>

    <ul class="contact lines">
      <li class="line line-phone"><span class="label">M</span><span>0438 596 204</span></li>
      <li class="line line-phone"><span class="label">P</span><span>07 4059 3827</span></li>
      <li class="line line-phone"><span class="label">F</span><span>07 4059 3828</span></li>
      <li class="line line-web"><span class="label">E</span><span>admin@corvanfab.com.au</span></li>
      <li class="line line-web"><span class="label">W</span><span>www.corvanfab.com.au</span></li>
    </ul>
  </div>
</body>
</html>
```